Fancy looking Inspection Postcard

Postcard needed for customers to inspect their product once it is delivered. We'll be giving them the steps for inspecting their product and to contact us if any issues arise. Would like to see something that sticks out but uses our company's colors. Would like to see creativity. Possibly utilizing the diamond steel background like we have in our logo.

Target Market(s)

Customers of our manufacturing shop

Industry/Entity Type

Manufacturing - metal wall art, custom products

Requirements
Must have
• our colors and logo
Nice to have
• get creative. i like creativity

```html
<!DOCTYPE html>
<html lang="en">
<head>
<meta charset="utf-8">
<title>Basalt Creek Fabrication – Inspection Postcard</title>
<link href="https://fonts.googleapis.com/css2?family=Roboto+Condensed:wght@300;400;700&display=swap" rel="stylesheet">
<style>
  :root {
    --stage: #c4c4c4;
    --steel: #262527;
    --steel-light: #333234;
    --yellow: #fff200;
    --ink: #1e1e1e;
    --white: #ffffff;
    --spark-dark: #1f5560;
    --spark-warm: #d9652e;
  }
  * { margin: 0; padding: 0; box-sizing: border-box; }
  html, body { width: 1200px; height: 1200px; overflow: hidden; }
  body {
    background: var(--stage);
    font-family: "Roboto Condensed", "Arial Narrow", sans-serif;
    position: relative;
  }
  .postcard {
    position: absolute;
    left: 233px;
    width: 733px;
    height: 489px;
    overflow: hidden;
    box-shadow: 0 4px 10px rgba(0,0,0,0.3);
  }
  .postcard--back { top: 62px; }
  .postcard--front { top: 631px; }
  .postcard svg.backdrop { position: absolute; inset: 0; }
  .abs { position: absolute; }

  /* back side */
  .brand-name {
    position: absolute;
    font-weight: 700;
    text-transform: uppercase;
    text-align: center;
    line-height: 1.05;
    color: var(--ink);
  }
  .back-brand { left: 191px; top: 70px; width: 160px; font-size: 22px; }
  .stamp-box {
    position: absolute; left: 606px; top: 46px; width: 82px; height: 94px;
    border: 1.5px solid var(--ink);
  }
  .contact-list { left: 39px; top: 186px; list-style: none; color: var(--white); font-weight: 300; font-size: 19px; }
  .contact-list li { display: flex; align-items: center; height: 32.5px; }
  .contact-list svg { width: 16px; height: 16px; margin-right: 10px; }
  .review-title { left: 36px; top: 289px; color: var(--yellow); font-size: 32px; font-weight: 400; letter-spacing: -0.3px; }
  .review-text { left: 38px; top: 332px; color: var(--white); font-weight: 300; font-size: 18.5px; line-height: 23px; }
  .review-contact { left: 37px; top: 390px; color: var(--yellow); font-size: 28px; line-height: 36px; }

  /* front side */
  .photo-area { position: absolute; left: 0; top: 0; width: 733px; height: 251px;
    background: linear-gradient(100deg, var(--spark-warm) 0%, #8a4a3a 45%, var(--spark-dark) 75%, #173f47 100%); }
  .front-brand { left: 40px; top: 75px; width: 200px; font-size: 24px; }
  .step {
    position: absolute; top: 251px; width: 183px; text-align: center; color: var(--ink);
  }
  .step-number { height: 43px; line-height: 45px; font-size: 30px; font-weight: 700; color: var(--yellow); letter-spacing: -0.5px; }
  .step-title { margin-top: 12px; font-size: 16px; font-weight: 700; line-height: 17px; text-transform: uppercase; }
  .step-text { margin-top: 15px; font-size: 13px; line-height: 16px; padding: 0 22px; }
</style>
</head>
<body>

<section class="postcard postcard--back">
  <svg class="backdrop" width="733" height="489" viewBox="0 0 733 489">
    <rect width="733" height="489" fill="var(--steel)"/>
    <path d="M124,0 C124,135 230,240 371,240 L371,489 L733,489 L733,0 Z" fill="var(--yellow)"/>
    <g stroke="var(--ink)" stroke-width="1.2">
      <line x1="426" y1="250" x2="688" y2="250"/>
      <line x1="426" y1="298" x2="688" y2="298"/>
      <line x1="426" y1="346" x2="688" y2="346"/>
      <line x1="426" y1="394" x2="688" y2="394"/>
      <line x1="426" y1="443" x2="688" y2="443"/>
    </g>
  </svg>
  <div class="brand-name back-brand">Basalt Creek Fabrication</div>
  <div class="stamp-box"></div>

  <ul class="contact-list abs">
    <li><svg viewBox="0 0 16 16"><rect x="4" y="1" width="8" height="14" rx="1.5" fill="none" stroke="var(--yellow)" stroke-width="1.6"/></svg>(555) 204-0190</li>
    <li><svg viewBox="0 0 16 16"><rect x="1" y="3" width="14" height="10" fill="var(--yellow)"/><path d="M1,3 L8,9 L15,3" fill="none" stroke="var(--steel)" stroke-width="1.2"/></svg>orders@basaltfab.com</li>
    <li><svg viewBox="0 0 16 16" fill="none" stroke="var(--yellow)" stroke-width="1.2"><circle cx="8" cy="8" r="6.5"/><ellipse cx="8" cy="8" rx="3" ry="6.5"/><line x1="1.5" y1="8" x2="14.5" y2="8"/></svg>www.basaltfab.com</li>
  </ul>
  <h2 class="review-title abs">DID WE DO A GOOD JOB?</h2>
  <p class="review-text abs">If you think so, leave us a review<br>on Mapsy? If not, Please let us know?</p>
  <p class="review-contact abs">info@basaltfab.com<br>555-476-0123</p>
</section>

<section class="postcard postcard--front">
  <div class="photo-area" role="img" aria-label="Photo of a metal worker in a hard hat grinding steel with a spray of orange sparks"></div>
  <svg class="backdrop" width="733" height="489" viewBox="0 0 733 489">
    <path d="M0,0 L264,0 C250,130 160,240 0,251 Z" fill="var(--ink)"/>
    <path d="M0,0 L257,0 C240,125 150,232 0,246 Z" fill="var(--white)"/>
    <rect y="251" width="733" height="238" fill="var(--steel)"/>
    <rect y="251" width="733" height="43" fill="var(--steel-light)"/>
    <rect y="294" width="733" height="63" fill="var(--yellow)"/>
    <g fill="var(--yellow)">
      <path d="M0,357 C0,410 50,452 92,487 C134,452 183,410 183,357 Z"/>
      <path d="M183,357 C183,410 233,452 275,487 C317,452 366,410 366,357 Z"/>
      <path d="M366,357 C366,410 416,452 458,487 C500,452 549,410 549,357 Z"/>
      <path d="M549,357 C549,410 599,452 641,487 C683,452 733,410 733,357 Z"/>
    </g>
    <g fill="none" stroke="var(--ink)" stroke-width="2.5">
      <path d="M20,355 C20,405 60,440 92,468 C124,440 164,405 164,355"/>
      <path d="M203,355 C203,405 243,440 275,468 C307,440 347,405 347,355"/>
      <path d="M386,355 C386,405 426,440 458,468 C490,440 530,405 530,355"/>
      <path d="M569,355 C569,405 609,440 641,468 C673,440 713,405 713,355"/>
    </g>
  </svg>
  <div class="brand-name front-brand">Basalt Creek Fabrication</div>

  <div class="step" style="left:0">
    <div class="step-number">STEP 1</div>
    <div class="step-title">Inspect<br>General Shape</div>
    <p class="step-text">Is it what you expected?<br>Is it bent, disoriented?</p>
  </div>
  <div class="step" style="left:183px">
    <div class="step-number">STEP 2</div>
    <div class="step-title">Inspect the welds<br>if there are any</div>
    <p class="step-text">Do they look clean?<br>Are there any gaps?</p>
  </div>
  <div class="step" style="left:366px">
    <div class="step-number">STEP 3</div>
    <div class="step-title">Inspect<br>the finish</div>
    <p class="step-text">Are there any areas not finished?<br>Are the colors what you expected?</p>
  </div>
  <div class="step" style="left:549px">
    <div class="step-number">STEP 4</div>
    <div class="step-title">Check for<br>functionality</div>
    <p class="step-text" style="line-height:20px">Does it work the way you want it tols it what you expected?</p>
  </div>
</section>

</body>
</html>
```